Bright Harbor Notes Wordpress Blog

I need to design a WordPress blog page. The name of the Blog is "Bright Harbor Notes". I am hoping for a simple design that is easy for me to post future posts to. I like the color teal for this. The website is brightharbornotes.example where I am going to write a personal blog. I don't have a logo for this, but am hoping for a header that has some swirly, but classy looking text. Easy on the eyes. The website will only have a couple of pages - the home landing page, and an about me page.

Font styles to use
Script

Colors
00a990
86cfc6
cfeae6

Requirements
Must have
• A header for the landing page of the blog. Clean layout of where the blog posts will lie.

```html
<!DOCTYPE html>
<html lang="en">
<head>
<meta charset="utf-8">
<title>Bright Harbor Notes</title>
<link rel="stylesheet" href="https://fonts.googleapis.com/css2?family=Inter:wght@300;400&family=Playball&display=swap">
<style>
  :root {
    --teal: #00a990;
    --teal-soft: #86cfc6;
    --teal-mist: #cfeae6;
    --teal-deep: #009680;
    --ink: #5d6c6c;
    --paper: #fefefe;
    --white: #ffffff;
  }
  html, body {
    margin: 0;
    padding: 0;
    overflow: hidden;
  }
  body {
    width: 1143px;
    height: 1200px;
    background: var(--paper);
    font-family: "Inter", "Helvetica Neue", Arial, sans-serif;
    font-weight: 300;
    color: var(--ink);
    position: relative;
  }
  .site-nav {
    position: absolute;
    top: 0;
    left: 0;
    width: 1143px;
    height: 85px;
    background: var(--white);
  }
  .site-nav a {
    position: absolute;
    top: 20px;
    font-size: 34px;
    line-height: 44px;
    text-decoration: none;
    transform: translateX(-50%);
    white-space: nowrap;
  }
  .nav-home { left: 370px; color: var(--ink); }
  .nav-about { left: 577px; color: var(--teal); }
  .nav-blog { left: 780px; color: var(--teal); }

  .hero {
    position: absolute;
    top: 85px;
    left: 0;
    width: 1143px;
    height: 586px;
  }
  .hero-backdrop,
  .footer-band {
    background: linear-gradient(180deg, var(--teal) 0%, #23b39c 45%, var(--teal-deep) 100%);
  }
  .hero-backdrop {
    position: absolute;
    inset: 0;
  }
  .hero-frame {
    position: absolute;
    left: 117px;
    top: 165px;
    width: 904px;
    height: 289px;
    border: 3px solid var(--white);
    box-sizing: border-box;
    text-align: center;
    color: var(--white);
  }
  .hero-title {
    margin: 0;
    position: absolute;
    top: 52px;
    left: 0;
    right: 0;
    font-family: "Playball", "Brush Script MT", cursive;
    font-weight: 400;
    font-size: 92px;
    line-height: 110px;
  }
  .hero-subtitle {
    margin: 0;
    position: absolute;
    top: 206px;
    left: 0;
    right: 0;
    font-size: 35px;
    line-height: 44px;
    color: var(--teal-mist);
  }

  .intro {
    position: absolute;
    top: 732px;
    left: 66px;
    width: 1011px;
    text-align: center;
  }
  .intro-title {
    margin: 0;
    font-weight: 300;
    font-size: 50px;
    line-height: 62px;
    color: var(--teal);
  }
  .intro-text {
    margin: 12px 0 0;
    font-size: 33px;
    line-height: 43.5px;
    color: var(--ink);
  }
  .blog-button {
    position: absolute;
    left: 415px;
    top: 981px;
    width: 309px;
    height: 79px;
    box-sizing: border-box;
    border: 3px solid var(--teal-soft);
    font-size: 52px;
    line-height: 72px;
    text-align: center;
    color: var(--ink);
    text-decoration: none;
  }
  .footer-band {
    position: absolute;
    left: 0;
    top: 1121px;
    width: 1143px;
    height: 79px;
  }
</style>
</head>
<body>
  <nav class="site-nav">
    <a class="nav-home" href="#">Home</a>
    <a class="nav-about" href="#">About Me</a>
    <a class="nav-blog" href="#">Blog</a>
  </nav>

  <header class="hero">
    <div class="hero-backdrop" role="img" aria-label="Teal-tinted wooden planks photograph as header background"></div>
    <div class="hero-frame">
      <h1 class="hero-title">Bright Harbor Notes</h1>
      <p class="hero-subtitle">| Calm notes on growth |</p>
    </div>
  </header>

  <main>
    <section class="intro">
      <h2 class="intro-title">Welcome Aboard</h2>
      <p class="intro-text">Welcome to my quiet harbor on the web. Here I share honest reflections, small lessons, weekly goals and the steady habits that help me grow, one simple post at a time.</p>
    </section>
    <a class="blog-button" href="#">Blog</a>
  </main>

  <footer class="footer-band" role="img" aria-label="Teal-tinted wooden planks photograph as footer band"></footer>
</body>
</html>
```